Guaranteed Job - Sleek Sexy Business Card UV Spot

Im looking for a sleek and sexy business card, that resembles elite or VIP status status.
our business is corinvale.example
you can view our products on there, but our main audience for handing out our cards will be for people in the hospitality industry, so it will need to impress high management and CEO of hotels and restaurants, bars, clubs etc...
the card features will have UV spot on both sides, 400gsm stock. standard size.
Artwork should be 86 x 54mm + 2mm bleed = 90 x 58mm
it should have a nice "unique" uv spot pattern that highlights the card, not a repeated pattern, theres no originality there, and it will be disregarded.
The written material will be:
Corin Vale Hospitality College (logo)
Tobin Marsh
Director
Phone: 1300 615 737
Mobile: 0455 817 296
Email: info@corinvale.example
website: www.corinvale.example
I'm looking for originality here, i don't want just a simple stock card, want something that has a wow factor for people.
You will find the logo attached. you may invert the white to black words to suit the background as you please.
thank you and good luck
As a side note, ive received a lot of proposals, im too busy to give feedback to each and every one, so if i havent provided feedback for your design within 24 hours, then consider it not acceptable, and you could resubmit another design.
So far i have not seen any design that stood out for me, they all seem pretty generic. there nothing thats unique, i would figure for the amount that im offering, that people would put some more effort and creativity into the design.
so far over 200 designs submitted, and nothing i have seen looks very original, everything looks like a different variation of the same stuff, i said it very clearly i wanted something unique, the only thing that has come close to it so far is this one
Reason: Ive received alot of design concepts and i have reviewed everyone, but i havent had time to give feedback to every single one, only the ones that have interested me, if i havent responded, its because i havent found it good enough.
so far only a few design have been on par with what ive been looking for, an attractive eye popping design.
heres a few of them,
http://files.pixelbazaar.example/design_img/51736/62418/62418_2840915_51736_image.jpg
http://files.pixelbazaar.example/design_img/51736/68254/68254_2841377_51736_image.jpg
theyre, both unique and original, and eye catching, the only thing theyre missing is the sexyness.
if you still think you have some creativity left in your minds, then throw it on here.
Reason: Sorry guys for the delay, I was in a serious accident and out of commission for the past few months, I'm just slowly recovering now, please bare with me as i try to attend to this project, it may take me awhile as I have other projects that are on standby, I'm not 100% at the moment, so im extending the deadline for 2 weeks right now. Thanks for your patience.
Hospitality

```html
<!DOCTYPE html>
<html lang="en">
<head>
<meta charset="utf-8">
<title>Corin Vale Hospitality College – Business Card</title>
<link rel="stylesheet" href="https://fonts.googleapis.com/css2?family=Bebas+Neue&family=Barlow+Semi+Condensed:wght@600&family=Quicksand:wght@400&display=swap">
<style>
  :root {
    --backdrop: #e3e3e1;
    --card-dark: #24282e;
    --card-dark-deep: #1c1f24;
    --accent-blue: #6a9fd6;
    --accent-blue-light: #86b3e2;
    --ink-white: #f4f5f6;
    --ink-grey: #8b8f95;
    --tile-dark: #1a1d22;
  }
  * { margin: 0; padding: 0; box-sizing: border-box; }
  html, body { width: 900px; height: 1200px; overflow: hidden; }
  body { background: var(--backdrop); position: relative; }

  .card {
    position: absolute;
    left: 100px;
    width: 700px;
    height: 440px;
    border-radius: 4px;
    overflow: hidden;
    box-shadow: 0 10px 28px rgba(0,0,0,0.22);
  }
  .card--front { top: 60px; background: linear-gradient(135deg, #2c3037, var(--card-dark-deep)); }
  .card--back { top: 700px; background: var(--card-dark); }

  /* Front */
  .brand {
    position: absolute;
    left: 250px;
    top: 160px;
    display: flex;
    align-items: center;
    gap: 22px;
  }
  .brand__mark { width: 70px; height: 70px; background: var(--accent-blue); }
  .brand__name {
    font-family: "Barlow Semi Condensed", sans-serif;
    font-weight: 600;
    color: var(--ink-white);
    text-transform: uppercase;
    line-height: 1;
  }
  .brand__name-main { display: block; font-size: 58px; letter-spacing: 1px; }
  .brand__name-sub { display: block; font-size: 21px; letter-spacing: 2px; margin-top: 6px; }

  /* Back */
  .back__band {
    position: absolute; left: 0; top: 0; bottom: 0; width: 190px;
    background: linear-gradient(180deg, var(--accent-blue-light), var(--accent-blue));
  }
  .back__flag { position: absolute; left: 150px; top: 40px; }
  .back__panel {
    position: absolute; left: 190px; top: 0; right: 0; bottom: 0;
    background: linear-gradient(160deg, #272b31, var(--card-dark-deep));
  }
  .person { position: absolute; left: 215px; top: 34px; font-family: "Bebas Neue", sans-serif; line-height: 0.9; }
  .person__name { font-size: 104px; color: var(--ink-white); letter-spacing: 1px; }
  .person__role { font-size: 44px; color: var(--ink-grey); letter-spacing: 1px; }

  .contacts { position: absolute; left: 150px; top: 250px; list-style: none; }
  .contacts__item { display: flex; align-items: center; height: 42px; }
  .contacts__key {
    width: 34px; height: 36px; border-radius: 5px;
    background: var(--tile-dark);
    color: var(--accent-blue);
    font-family: "Bebas Neue", sans-serif;
    font-size: 30px;
    display: flex; align-items: center; justify-content: center;
    padding-top: 3px;
  }
  .contacts__value {
    margin-left: 24px;
    font-family: "Quicksand", sans-serif;
    font-size: 25px;
    color: var(--ink-white);
  }
</style>
</head>
<body>

  <section class="card card--front" aria-label="Card front">
    <div class="brand">
      <span class="brand__mark" aria-hidden="true"></span>
      <h1 class="brand__name">
        <span class="brand__name-main">Corin Vale</span>
        <span class="brand__name-sub">Hospitality College</span>
      </h1>
    </div>
  </section>

  <section class="card card--back" aria-label="Card back">
    <div class="back__band"></div>
    <div class="back__panel"></div>
    <svg class="back__flag" width="44" height="40" viewBox="0 0 44 40" aria-hidden="true">
      <polygon points="0,40 22,0 44,0 44,40" fill="#262a30"/>
    </svg>

    <div class="person">
      <h2 class="person__name">Tobin Marsh</h2>
      <p class="person__role">Director</p>
    </div>

    <ul class="contacts">
      <li class="contacts__item"><span class="contacts__key">P</span><span class="contacts__value">1300 615 737</span></li>
      <li class="contacts__item"><span class="contacts__key">M</span><span class="contacts__value">0455 817 296</span></li>
      <li class="contacts__item"><span class="contacts__key">E</span><span class="contacts__value">info@corinvale.example</span></li>
      <li class="contacts__item"><span class="contacts__key">W</span><span class="contacts__value">www.corinvale.example</span></li>
    </ul>
  </section>

</body>
</html>
```